Music School needs Calendar Design

Need Calendar design for a music school. Calendar is a small desktop calendar. Calendar is a flip calendar about 4" x 8" with a base. Very open-ended, just want something that's classy and simple. In the past we've used a theme, like 12 composers, 12 instruments, 12 styles of music, etc...

Industry/Entity Type

School

Font styles to use
Decorative

Requirements
Must have
• Will need to design calendar pages and base. Base fairly straightforward since it just contains contact info. There are some dates that need to be highlighted that are not national holidays

```html
<!DOCTYPE html>
<html lang="en">
<head>
<meta charset="utf-8">
<title>2017 Music School Desk Calendar</title>
<link rel="stylesheet" href="https://fonts.googleapis.com/css2?family=Caveat:wght@400&family=Courier+Prime&family=Kalam:wght@300&display=swap">
<style>
:root{
  --ink:#111;
  --red:#e3141b;
  --paper:#fbfbfb;
  --jan:#67c3d3;--feb:#ffc800;--mar:#b09a7c;--apr:#ff6a00;
  --may:#33cc33;--jun:#f2b3b6;--jul:#8a8a8a;--aug:#b5af8a;
  --sep:#d3cfe6;--oct:#c795c9;--nov:#ccff66;--dec:#e0191f;
}
*{box-sizing:border-box;margin:0;padding:0}
html,body{width:1200px;height:1200px;overflow:hidden;background:#fff}
.canvas{position:relative;width:1200px;height:1200px}
.page{position:absolute;font-size:10px;width:25.4em;height:18.7em;overflow:hidden;
  background:radial-gradient(ellipse at 35% 55%,rgba(255,255,255,.35),rgba(255,255,255,0) 60%),var(--bg);
  box-shadow:0 0 .3em rgba(0,0,0,.35)}
.page--feature{font-size:20px;left:346px;top:50px}
.page-strip{position:absolute;left:0;top:0;width:100%;height:1.9em;
  background:repeating-linear-gradient(90deg,transparent 0 .4em,var(--ink) .4em 1em,transparent 1em 1.1em);
  background-size:1.1em .7em;background-repeat:repeat-x;background-position:.3em .6em}
.page-band{position:absolute;left:0;top:1.9em;width:100%;height:2.6em;background:var(--ink);color:#fff}
.page-year{position:absolute;left:13%;top:0;font-family:"Kalam",cursive;font-weight:300;font-size:2em;line-height:1.3}
.page-month{position:absolute;right:14%;top:.25em;font-family:"Caveat",cursive;font-weight:400;font-size:1.5em;line-height:1.3}
.month-card{position:absolute;left:2.1em;top:6.4em;width:11.5em;height:9.8em;background:var(--paper);
  box-shadow:0 .25em .4em rgba(0,0,0,.25);padding:.6em .9em 0;text-align:center;font-family:"Courier Prime",monospace}
.month-card h2{font-weight:400;color:var(--red);font-size:1.1em;letter-spacing:.05em;line-height:1.1}
.days{display:grid;grid-template-columns:repeat(7,1fr);row-gap:.35em;margin-top:.3em;font-family:Arial,sans-serif;font-size:.5em;color:var(--ink)}
.days span,.days i{font-style:normal}
.days > :nth-child(7n+1),.days > :nth-child(7n){color:var(--red)}
.days .dow{font-size:.9em;margin-bottom:.8em}
.days .pair{font-size:.75em;letter-spacing:-.05em}
.illustration{position:absolute;left:14.6em;top:5.6em;width:10.2em;height:11em;border-radius:1em;
  background:radial-gradient(ellipse at center,rgba(0,0,0,.28),rgba(0,0,0,.05) 70%,transparent 72%)}
.page-footer{position:absolute;left:0;right:0;bottom:.5em;text-align:center;font-family:"Caveat",cursive;font-size:.75em;line-height:1.2;white-space:nowrap;color:var(--ink)}
.page-footer span{margin:0 .8em}
.thumb--1{left:46px;top:490px}.thumb--2{left:330px;top:490px}.thumb--3{left:614px;top:490px}.thumb--4{left:899px;top:490px}
.thumb--5{left:46px;top:720px}.thumb--6{left:330px;top:720px}.thumb--7{left:614px;top:720px}.thumb--8{left:899px;top:720px}
.thumb--9{left:46px;top:950px}.thumb--10{left:330px;top:950px}.thumb--11{left:614px;top:950px}.thumb--12{left:899px;top:950px}
.jan{--bg:var(--jan)}.feb{--bg:var(--feb)}.mar{--bg:var(--mar)}.apr{--bg:var(--apr)}
.may{--bg:var(--may)}.jun{--bg:var(--jun)}.jul{--bg:var(--jul)}.aug{--bg:var(--aug)}
.sep{--bg:var(--sep)}.oct{--bg:var(--oct)}.nov{--bg:var(--nov)}.dec{--bg:var(--dec)}
</style>
</head>
<body>
<main class="canvas">

<section class="page page--feature jan">
  <div class="page-strip"></div>
  <div class="page-band"><span class="page-year">2017</span><span class="page-month">January</span></div>
  <div class="month-card"><h2>January</h2>
    <div class="days"><span class="dow">Sun</span><span class="dow">Mon</span><span class="dow">Tue</span><span class="dow">Wed</span><span class="dow">Thu</span><span class="dow">Fri</span><span class="dow">Sat</span>
    <span>1</span><span>2</span><span>3</span><span>4</span><span>5</span><span>6</span><span>7</span><span>8</span><span>9</span><span>10</span><span>11</span><span>12</span><span>13</span><span>14</span><span>15</span><span>16</span><span>17</span><span>18</span><span>19</span><span>20</span><span>21</span><span>22</span><span>23</span><span>24</span><span>25</span><span>26</span><span>27</span><span>28</span><span>29</span><span>30</span><span>31</span></div>
  </div>
  <div class="illustration" role="img" aria-label="Line drawing of two cartoon cats playing violin and piano with music notes"></div>
  <p class="page-footer"><span>Adress: Lorem ipsum dolor sit amet, consectetur adipiscing</span><span>Telephone: 01 23 456 789 00</span></p>
</section>

<section class="page thumb--1 jan">
  <div class="page-strip"></div>
  <div class="page-band"><span class="page-year">2017</span><span class="page-month">January</span></div>
  <div class="month-card"><h2>January</h2>
    <div class="days"><span class="dow">Sun</span><span class="dow">Mon</span><span class="dow">Tue</span><span class="dow">Wed</span><span class="dow">Thu</span><span class="dow">Fri</span><span class="dow">Sat</span>
    <span>1</span><span>2</span><span>3</span><span>4</span><span>5</span><span>6</span><span>7</span><span>8</span><span>9</span><span>10</span><span>11</span><span>12</span><span>13</span><span>14</span><span>15</span><span>16</span><span>17</span><span>18</span><span>19</span><span>20</span><span>21</span><span>22</span><span>23</span><span>24</span><span>25</span><span>26</span><span>27</span><span>28</span><span>29</span><span>30</span><span>31</span></div>
  </div>
  <div class="illustration" role="img" aria-label="Line drawing of two cats playing violin and piano"></div>
</section>

<section class="page thumb--2 feb">
  <div class="page-strip"></div>
  <div class="page-band"><span class="page-year">2017</span><span class="page-month">February</span></div>
  <div class="month-card"><h2>February</h2>
    <div class="days"><span class="dow">Sun</span><span class="dow">Mon</span><span class="dow">Tue</span><span class="dow">Wed</span><span class="dow">Thu</span><span class="dow">Fri</span><span class="dow">Sat</span>
    <i></i><i></i><i></i><span>1</span><span>2</span><span>3</span><span>4</span><span>5</span><span>6</span><span>7</span><span>8</span><span>9</span><span>10</span><span>11</span><span>12</span><span>13</span><span>14</span><span>15</span><span>16</span><span>17</span><span>18</span><span>19</span><span>20</span><span>21</span><span>22</span><span>23</span><span>24</span><span>25</span><span>26</span><span>27</span><span>28</span></div>
  </div>
  <div class="illustration" role="img" aria-label="Line drawing of two birds playing a tuba and a banjo"></div>
</section>

<section class="page thumb--3 mar">
  <div class="page-strip"></div>
  <div class="page-band"><span class="page-year">2017</span><span class="page-month">March</span></div>
  <div class="month-card"><h2>March</h2>
    <div class="days"><span class="dow">Sun</span><span class="dow">Mon</span><span class="dow">Tue</span><span class="dow">Wed</span><span class="dow">Thu</span><span class="dow">Fri</span><span class="dow">Sat</span>
    <i></i><i></i><i></i><span>1</span><span>2</span><span>3</span><span>4</span><span>5</span><span>6</span><span>7</span><span>8</span><span>9</span><span>10</span><span>11</span><span>12</span><span>13</span><span>14</span><span>15</span><span>16</span><span>17</span><span>18</span><span>19</span><span>20</span><span>21</span><span>22</span><span>23</span><span>24</span><span>25</span><span>26</span><span>27</span><span>28</span><span>29</span><span>30</span><span>31</span></div>
  </div>
  <div class="illustration" role="img" aria-label="Line drawing of a trumpet player"></div>
</section>

<section class="page thumb--4 apr">
  <div class="page-strip"></div>
  <div class="page-band"><span class="page-year">2017</span><span class="page-month">April</span></div>
  <div class="month-card"><h2>April</h2>
    <div class="days"><span class="dow">Sun</span><span class="dow">Mon</span><span class="dow">Tue</span><span class="dow">Wed</span><span class="dow">Thu</span><span class="dow">Fri</span><span class="dow">Sat</span>
    <i></i><i></i><i></i><i></i><i></i><i></i><span>1</span><span>2</span><span>3</span><span>4</span><span>5</span><span>6</span><span>7</span><span>8</span><span>9</span><span>10</span><span>11</span><span>12</span><span>13</span><span>14</span><span>15</span><span>16</span><span>17</span><span>18</span><span>19</span><span>20</span><span>21</span><span>22</span><span class="pair">23/30</span><span>24</span><span>25</span><span>26</span><span>27</span><span>28</span><span>29</span></div>
  </div>
  <div class="illustration" role="img" aria-label="Line drawing of three singers in a bathtub"></div>
</section>

<section class="page thumb--5 may">
  <div class="page-strip"></div>
  <div class="page-band"><span class="page-year">2017</span><span class="page-month">May</span></div>
  <div class="month-card"><h2>May</h2>
    <div class="days"><span class="dow">Sun</span><span class="dow">Mon</span><span class="dow">Tue</span><span class="dow">Wed</span><span class="dow">Thu</span><span class="dow">Fri</span><span class="dow">Sat</span>
    <i></i><span>1</span><span>2</span><span>3</span><span>4</span><span>5</span><span>6</span><span>7</span><span>8</span><span>9</span><span>10</span><span>11</span><span>12</span><span>13</span><span>14</span><span>15</span><span>16</span><span>17</span><span>18</span><span>19</span><span>20</span><span>21</span><span>22</span><span>23</span><span>24</span><span>25</span><span>26</span><span>27</span><span>28</span><span>29</span><span>30</span><span>31</span></div>
  </div>
  <div class="illustration" role="img" aria-label="Line drawing of a rock band with guitars and drums"></div>
</section>

<section class="page thumb--6 jun">
  <div class="page-strip"></div>
  <div class="page-band"><span class="page-year">2017</span><span class="page-month">June</span></div>
  <div class="month-card"><h2>June</h2>
    <div class="days"><span class="dow">Sun</span><span class="dow">Mon</span><span class="dow">Tue</span><span class="dow">Wed</span><span class="dow">Thu</span><span class="dow">Fri</span><span class="dow">Sat</span>
    <i></i><i></i><i></i><i></i><span>1</span><span>2</span><span>3</span><span>4</span><span>5</span><span>6</span><span>7</span><span>8</span><span>9</span><span>10</span><span>11</span><span>12</span><span>13</span><span>14</span><span>15</span><span>16</span><span>17</span><span>18</span><span>19</span><span>20</span><span>21</span><span>22</span><span>23</span><span>24</span><span>25</span><span>26</span><span>27</span><span>28</span><span>29</span><span>30</span></div>
  </div>
  <div class="illustration" role="img" aria-label="Line drawing of two dancing dogs"></div>
</section>

<section class="page thumb--7 jul">
  <div class="page-strip"></div>
  <div class="page-band"><span class="page-year">2017</span><span class="page-month">July</span></div>
  <div class="month-card"><h2>July</h2>
    <div class="days"><span class="dow">Sun</span><span class="dow">Mon</span><span class="dow">Tue</span><span class="dow">Wed</span><span class="dow">Thu</span><span class="dow">Fri</span><span class="dow">Sat</span>
    <i></i><i></i><i></i><i></i><i></i><i></i><span>1</span><span>2</span><span>3</span><span>4</span><span>5</span><span>6</span><span>7</span><span>8</span><span>9</span><span>10</span><span>11</span><span>12</span><span>13</span><span>14</span><span>15</span><span>16</span><span>17</span><span>18</span><span>19</span><span>20</span><span>21</span><span>22</span><span class="pair">23/30</span><span class="pair">24/31</span><span>25</span><span>26</span><span>27</span><span>28</span><span>29</span></div>
  </div>
  <div class="illustration" role="img" aria-label="Line drawing of a cat in sunglasses playing violin"></div>
</section>

<section class="page thumb--8 aug">
  <div class="page-strip"></div>
  <div class="page-band"><span class="page-year">2017</span><span class="page-month">August</span></div>
  <div class="month-card"><h2>August</h2>
    <div class="days"><span class="dow">Sun</span><span class="dow">Mon</span><span class="dow">Tue</span><span class="dow">Wed</span><span class="dow">Thu</span><span class="dow">Fri</span><span class="dow">Sat</span>
    <i></i><i></i><span>1</span><span>2</span><span>3</span><span>4</span><span>5</span><span>6</span><span>7</span><span>8</span><span>9</span><span>10</span><span>11</span><span>12</span><span>13</span><span>14</span><span>15</span><span>16</span><span>17</span><span>18</span><span>19</span><span>20</span><span>21</span><span>22</span><span>23</span><span>24</span><span>25</span><span>26</span><span>27</span><span>28</span><span>29</span><span>30</span><span>31</span></div>
  </div>
  <div class="illustration" role="img" aria-label="Line drawing of a duck playing a banjo"></div>
</section>

<section class="page thumb--9 sep">
  <div class="page-strip"></div>
  <div class="page-band"><span class="page-year">2017</span><span class="page-month">September</span></div>
  <div class="month-card"><h2>September</h2>
    <div class="days"><span class="dow">Sun</span><span class="dow">Mon</span><span class="dow">Tue</span><span class="dow">Wed</span><span class="dow">Thu</span><span class="dow">Fri</span><span class="dow">Sat</span>
    <i></i><i></i><i></i><i></i><i></i><span>1</span><span>2</span><span>3</span><span>4</span><span>5</span><span>6</span><span>7</span><span>8</span><span>9</span><span>10</span><span>11</span><span>12</span><span>13</span><span>14</span><span>15</span><span>16</span><span>17</span><span>18</span><span>19</span><span>20</span><span>21</span><span>22</span><span>23</span><span>24</span><span>25</span><span>26</span><span>27</span><span>28</span><span>29</span><span>30</span></div>
  </div>
  <div class="illustration" role="img" aria-label="Line drawing of a marching drummer and trumpeter"></div>
</section>

<section class="page thumb--10 oct">
  <div class="page-strip"></div>
  <div class="page-band"><span class="page-year">2017</span><span class="page-month">October</span></div>
  <div class="month-card"><h2>October</h2>
    <div class="days"><span class="dow">Sun</span><span class="dow">Mon</span><span class="dow">Tue</span><span class="dow">Wed</span><span class="dow">Thu</span><span class="dow">Fri</span><span class="dow">Sat</span>
    <span>1</span><span>2</span><span>3</span><span>4</span><span>5</span><span>6</span><span>7</span><span>8</span><span>9</span><span>10</span><span>11</span><span>12</span><span>13</span><span>14</span><span>15</span><span>16</span><span>17</span><span>18</span><span>19</span><span>20</span><span>21</span><span>22</span><span>23</span><span>24</span><span>25</span><span>26</span><span>27</span><span>28</span><span>29</span><span>30</span><span>31</span></div>
  </div>
  <div class="illustration" role="img" aria-label="Line drawing of a fiddler and a small dog"></div>
</section>

<section class="page thumb--11 nov">
  <div class="page-strip"></div>
  <div class="page-band"><span class="page-year">2017</span><span class="page-month">November</span></div>
  <div class="month-card"><h2>November</h2>
    <div class="days"><span class="dow">Sun</span><span class="dow">Mon</span><span class="dow">Tue</span><span class="dow">Wed</span><span class="dow">Thu</span><span class="dow">Fri</span><span class="dow">Sat</span>
    <i></i><i></i><i></i><span>1</span><span>2</span><span>3</span><span>4</span><span>5</span><span>6</span><span>7</span><span>8</span><span>9</span><span>10</span><span>11</span><span>12</span><span>13</span><span>14</span><span>15</span><span>16</span><span>17</span><span>18</span><span>19</span><span>20</span><span>21</span><span>22</span><span>23</span><span>24</span><span>25</span><span>26</span><span>27</span><span>28</span><span>29</span><span>30</span></div>
  </div>
  <div class="illustration" role="img" aria-label="Line drawing of two violinists"></div>
</section>

<section class="page thumb--12 dec">
  <div class="page-strip"></div>
  <div class="page-band"><span class="page-year">2017</span><span class="page-month">December</span></div>
  <div class="month-card"><h2>December</h2>
    <div class="days"><span class="dow">Sun</span><span class="dow">Mon</span><span class="dow">Tue</span><span class="dow">Wed</span><span class="dow">Thu</span><span class="dow">Fri</span><span class="dow">Sat</span>
    <i></i><i></i><i></i><i></i><i></i><span>1</span><span>2</span><span>3</span><span>4</span><span>5</span><span>6</span><span>7</span><span>8</span><span>9</span><span>10</span><span>11</span><span>12</span><span>13</span><span>14</span><span>15</span><span>16</span><span>17</span><span>18</span><span>19</span><span>20</span><span>21</span><span>22</span><span>23</span><span class="pair">24/31</span><span>25</span><span>26</span><span>27</span><span>28</span><span>29</span><span>30</span></div>
  </div>
  <div class="illustration" role="img" aria-label="Line drawing of a trio of carol singers"></div>
</section>

</main>
</body>
</html>
```